Outpost Lattice Advisors – Franchise Growth & Development Presentation

Outpost Lattice Advisors is an outsourced franchise sales organization (FSO) that helps franchisors grow their franchise systems without the expense and risk of hiring an internal franchise development team.

We are seeking a professional PowerPoint presentation that will be used to present our services to franchisors, franchise executives, founders, and growth-stage franchise brands.

The presentation should communicate the value of partnering with Outpost Lattice Advisors, including:

• Fractional franchise sales team versus hiring internal staff
• 30+ years of franchise industry experience
• 550+ franchise sales successes
• Immediate access to established franchise broker relationships
• Proven franchise development processes
• Franchise growth strategy and enterprise value creation
• Potential private equity and exit opportunities through franchise expansion

The presentation should feel like a modern consulting, investment, or growth strategy presentation rather than a typical sales brochure. We want strong visual storytelling, custom infographics, professional diagrams, and clean business-oriented design.

The audience includes business owners, franchise founders, franchise executives, and investors who are evaluating growth strategies for their franchise systems.

Target Market(s)

Primary Audience: Emerging franchisors Growth-stage franchise brands Franchise founders Franchise CEOs Franchise presidents Franchise development executives Secondary Audience: Private equity firms Franchise investors Strategic buyers Franchise consultants

Industry/Entity Type

Franchise Development, Private Equity / Business Expansion

Font styles to use
Other font styles liked:
• Use Montserrat for titles and Open Sans for body text.

Requirements
Must have
• Modern professional business design Consistent branding throughout Custom infographics Comparison graphics Broker network ecosystem graphic Enterprise value graphic Easy-to-read charts and visuals Editable PowerPoint format Professional iconography. www.outpostlatticeadvisors.example as reference for colors
Nice to have
• Franchise-related imagery Subtle growth-themed visuals Timeline graphics Data visualization Private equity / valuation style graphics
Should not have
• Cartoon graphics Clip art Overly busy slides Stock-template appearance Bright neon colors Handwritten fonts Excessive text on slides Juvenile or playful design elements

```html
<!DOCTYPE html>
<html lang="en">
<head>
<meta charset="utf-8">
<title>Building Enterprise Value Through Franchise Growth</title>
<link href="https://fonts.googleapis.com/css2?family=Montserrat:wght@500;600;700;800&family=Rubik:wght@400;500&display=swap" rel="stylesheet">
<style>
:root{
  --navy:#0b2744;
  --orange:#f7941d;
  --header-grey:#dfe4ea;
  --line:#c9ced4;
  --ink:#14243a;
  --white:#ffffff;
}
*{margin:0;padding:0;box-sizing:border-box}
html,body{width:1200px;height:675px;overflow:hidden;background:var(--white)}
body{position:relative;font-family:'Rubik',sans-serif;color:var(--ink)}
.slide-title{position:absolute;left:77px;top:48px;font-family:'Montserrat',sans-serif;font-weight:800;font-size:31px;line-height:39px;letter-spacing:.3px}
.slide-title .line-navy{color:var(--navy);display:block}
.slide-title .line-orange{color:var(--orange);display:block}
.title-rule{position:absolute;left:85px;top:134px;width:312px;height:3px;background:linear-gradient(90deg,var(--orange),rgba(247,148,29,.1));border-radius:2px}
.intro{position:absolute;left:667px;top:66px;width:460px;font-size:20.5px;line-height:26px;color:var(--ink)}
.card{position:absolute;top:181px;width:527px;height:208px;border:1px solid var(--line);background:var(--white)}
.card.scenario{left:77px}
.card.valuation{left:621px}
.card-head{height:56px;padding-left:36px;display:flex;align-items:center;font-family:'Montserrat',sans-serif;font-weight:700;font-size:21px;color:var(--white)}
.scenario .card-head{background:var(--navy)}
.valuation .card-head{background:var(--orange)}
.card table{width:100%;border-collapse:collapse}
.card th{background:var(--header-grey);height:43px;text-align:left;font-family:'Montserrat',sans-serif;font-weight:700;font-size:13px;color:var(--navy)}
.card td{height:40px;font-size:16px;border-bottom:1px solid var(--line)}
.card tr:last-child td{border-bottom:none}
.card th:first-child,.card td:first-child{padding-left:36px}
.takeaway{position:absolute;left:76px;top:418px;width:1073px;height:137px;border:1px solid var(--line);border-left:4px solid var(--orange);padding:24px 0 0 35px}
.takeaway h2{font-family:'Montserrat',sans-serif;font-weight:800;font-size:20px;color:var(--navy);margin-bottom:6px}
.takeaway p{font-size:17.5px;line-height:26px;color:var(--ink)}
.footer-brand{position:absolute;left:57px;top:622px;font-family:'Montserrat',sans-serif;font-weight:800;font-size:17px;color:var(--navy);letter-spacing:.2px}
.footer-rule{position:absolute;left:257px;top:634px;width:870px;height:4px;background:repeating-linear-gradient(90deg,#c4c8cd 0 1px,transparent 1px 3px)}
.page-num{position:absolute;left:1124px;top:619px}
.bottom-band{position:absolute;left:0;bottom:0;width:1172px;height:4px;background:linear-gradient(90deg,var(--navy) 0 33%,var(--orange) 33% 100%)}
</style>
</head>
<body>
<h1 class="slide-title"><span class="line-navy">BUILDING ENTERPRISE VALUE</span><span class="line-orange">THROUGH FRANCHISE GROWTH</span></h1>
<div class="title-rule"></div>
<p class="intro">Franchise growth creates recurring royalty revenue and increases enterprise value.</p>

<section class="card scenario">
  <div class="card-head">Example Growth Scenario</div>
  <table>
    <tr><th style="width:168px">Stage</th><th style="width:124px">Units</th><th>Annual Royalty Revenue</th></tr>
    <tr><td>Early Growth</td><td>20</td><td>$165,000</td></tr>
    <tr><td>Growth Stage</td><td>63</td><td>$1,470,000</td></tr>
  </table>
</section>

<section class="card valuation">
  <div class="card-head">Illustrative Valuation Range</div>
  <table>
    <tr><th style="width:215px">Royalty Revenue</th><th style="width:158px">10x EBITDA</th><th>15x EBITDA</th></tr>
    <tr><td>$165,000</td><td>$1.65M</td><td>$2.48M</td></tr>
    <tr><td>$1,470,000</td><td>$14.7M</td><td>$22.05M</td></tr>
  </table>
</section>

<section class="takeaway">
  <h2>KEY TAKEAWAY</h2>
  <p>Franchise growth is not just about selling franchises.<br>It is about creating recurring royalty revenue that can significantly increase the value of the franchise system.</p>
</section>

<div class="footer-brand">Outpost Lattice Advisors</div>
<div class="footer-rule"></div>
<svg class="page-num" width="36" height="32" viewBox="0 0 36 32" aria-label="Page 12">
  <polygon points="9,1 27,1 35,16 27,31 9,31 1,16" fill="#f7941d"/>
  <text x="18" y="21.5" text-anchor="middle" font-family="Montserrat, sans-serif" font-weight="700" font-size="14" fill="#fff">12</text>
</svg>
<div class="bottom-band"></div>
</body>
</html>
```